explains reason for march on Washington, DC

Important...I would like this to be an "oversized" card, but when I picked that choice, then having you design the card was not available. I hope this can still work.

This is not a business card. I will hand it to people who ask me about my idea to organize a march in Washington. On one side of the card will be a picture of Brookhaven Cemetery with the following words superimposed on the photo-(I want the graves to take center stage, with the words secondary)-the words are: "These men and women can, no longer, preserve our freedom." "That job now belongs to we, the living."

On the other side is this text:

If I am giving you this card, you have heard about my idea. I am following through on my idea to occupy the Senate and House Chambers on Memorial Day because I love America and the freedom that it has showered on me, a freedom that I see as being in great peril.

So, I am taking a stand.

You are free, of course, to think what you want about what I am doing. I am not looking for an argument, just a resolution about the future of the greatest nation on earth. To commit to joining this effort, go to forlucinda.example.

Thank you.
Ted Marlow

You can be creative with the layout for these words.

Thank you.

Reason: I have been asked for a photo that is taking additional time. Thank you.

Hi.  The current deadline is for Feb. 27th, but I need to change it to this Saturday, Feb. 22nd.  My timeline has changed.  Please make submissions by 5 p.m. on Saturday.  That is my cut-off time and date.  Thank you.  Ted

```html
<!DOCTYPE html>
<html lang="en">
<head>
<meta charset="utf-8">
<title>Memorial Day Card – The Living</title>
<link rel="stylesheet" href="https://fonts.googleapis.com/css2?family=Bodoni+Moda:opsz,wght@6..96,400;6..96,700&display=swap">
<style>
  :root {
    --backdrop: #ece8e2;
    --band-grey: #7b7b80;
    --panel-charcoal: #58595b;
    --paper-white: #ffffff;
    --ink-white: #ffffff;
    --rule-grey: #4a4a4a;
    --photo-sky: #d9dcdc;
    --photo-trees: #6f7a58;
    --photo-grass: #5f8a3a;
  }
  * { box-sizing: border-box; margin: 0; padding: 0; }
  html, body { width: 1200px; height: 1000px; overflow: hidden; }
  body {
    background: var(--backdrop);
    position: relative;
    font-family: "Bodoni Moda", "Didot", serif;
  }

  /* Front of card */
  .card-front {
    position: absolute;
    left: 112px; top: 74px;
    width: 610px; height: 474px;
    overflow: hidden;
    box-shadow: 0 2px 8px rgba(0,0,0,0.18);
  }
  .cemetery-photo {
    position: absolute; inset: 0;
    background: linear-gradient(180deg,
      var(--photo-sky) 0%,
      #b9bdb3 25%,
      var(--photo-trees) 55%,
      #4d5a3e 72%,
      var(--photo-grass) 82%,
      #e6e6e2 100%);
  }
  .quote-band {
    position: absolute;
    left: 78px; top: 81px;
    width: 532px; height: 138px;
    background: var(--band-grey);
    color: var(--ink-white);
  }
  .quote-mark {
    position: absolute;
    font-weight: 700;
    font-size: 92px;
    line-height: 1;
  }
  .quote-mark--open { left: 12px; top: 10px; }
  .quote-mark--close { left: 430px; top: 62px; }
  .quote-lead {
    position: absolute;
    left: 87px; top: 25px;
    font-size: 15px;
    line-height: 21px;
    letter-spacing: 0.2px;
  }
  .quote-emphasis {
    position: absolute;
    left: 86px; top: 70px;
    font-size: 43px;
    letter-spacing: 3px;
    line-height: 1.1;
  }

  /* Back of card */
  .card-back {
    position: absolute;
    left: 509px; top: 437px;
    width: 612px; height: 475px;
    display: flex;
    box-shadow: 0 2px 8px rgba(0,0,0,0.18);
  }
  .message-panel {
    width: 296px;
    background: var(--panel-charcoal);
    color: var(--ink-white);
    padding: 19px 20px 0 33px;
    font-size: 11.4px;
    line-height: 16.6px;
  }
  .message-panel p { margin-bottom: 16.6px; }
  .call-to-action { text-align: center; margin-bottom: 8px !important; }
  .site-link {
    display: block;
    width: max-content;
    margin: 0 auto 22px;
    padding: 0 4px 1px;
    font-size: 14.5px;
    font-weight: 700;
    letter-spacing: 0.3px;
    border-bottom: 1px solid var(--ink-white);
  }
  .sign-off { margin-bottom: 0 !important; }
  .address-panel {
    flex: 1;
    background: var(--paper-white);
    position: relative;
  }
  .address-lines {
    position: absolute;
    left: 31px; top: 206px;
  }
</style>
</head>
<body>

  <section class="card-front" aria-label="Card front">
    <div class="cemetery-photo" role="img" aria-label="Photograph of a military funeral procession with a horse-drawn caisson passing rows of white headstones at Brookhaven Cemetery"></div>
    <div class="quote-band">
      <span class="quote-mark quote-mark--open">&ldquo;</span>
      <p class="quote-lead">Our fallen heroes can no longer preserve our freedom.<br>That job now belongs to us,</p>
      <p class="quote-emphasis">THE LIVING.</p>
      <span class="quote-mark quote-mark--close">&rdquo;</span>
    </div>
  </section>

  <section class="card-back" aria-label="Card back">
    <div class="message-panel">
      <p>If I am giving you this card, you have heard about my idea. I am following through on my idea to occupy the Senate and House Chambers on Memorial Day because I love America and the freedom that it has showered on me, a freedom that I see as being in great peril.</p>
      <p>So, I am taking a stand.</p>
      <p>You are free, of course, to think what you want about what I am doing. I am not looking for an argument, just a resolution about the future of the greatest nation on earth.</p>
      <p class="call-to-action">If you support my idea, then commit<br>yourself to this effort at</p>
      <span class="site-link">www.forlucinda.example</span>
      <p class="sign-off">Thank you.<br>Ted Marlow</p>
    </div>
    <div class="address-panel">
      <svg class="address-lines" width="246" height="134" viewBox="0 0 246 134" aria-hidden="true">
        <g stroke="var(--rule-grey)" stroke-width="1.3">
          <line x1="0" y1="1" x2="245" y2="1"/>
          <line x1="0" y1="27" x2="245" y2="27"/>
          <line x1="0" y1="53" x2="245" y2="53"/>
          <line x1="0" y1="79" x2="245" y2="79"/>
          <line x1="0" y1="105" x2="245" y2="105"/>
          <line x1="0" y1="131" x2="245" y2="131"/>
        </g>
      </svg>
    </div>
  </section>

</body>
</html>
```